Website Design For Atelier Nine Design Group

Create a sophisticated website that denotes high-end luxury. We would like to keep the copy minimalist and elegantly understated while communicating only the most essential information. While creating an air of exclusivity.
We would like 3-4 Tab Wesbite
Home:
• Feature a design project front and centre, along with a short
introduction about who we are and what we do.

We can put a Call To Action at the end of the introduction inviting readers to learn more on our About page.
About:
• This page should provide more detail on our background, past
achievements, history of the company, and anything you'd like to
highlight.
• We should also provide details on our services, aesthetic, process, etc.
Team:
• introduce the team, possibly with short descriptions for each
team member. Total Team Members 7
Residential
• The portfolio page can be a grid of images along with titles for
each project.
• Clicking on each image should take you to a separate page for that
project where readers can find more details

Commercial
The portfolio page can be a grid of images along with titles for
each project.

Contact Us:

example website:
https://www.morvexinteriors.example/

Target Market(s)

High end luxury clientele

Industry/Entity Type

Interior Design

Number of Pages Required

4 page

Font styles to use
Sans Serif

Requirements
Must have
• Company logo, color scheme and name: Atelier Nine Design Group

```html
<!DOCTYPE html>
<html lang="en">
<head>
<meta charset="utf-8">
<title>Atelier Nine Design Group</title>
<link href="https://fonts.googleapis.com/css2?family=Lato:wght@400;700&family=Montserrat:wght@300;400;500;600&family=Open+Sans:wght@700&display=swap" rel="stylesheet">
<style>
:root{
  --navy:#0b4560;
  --navy-deep:#0e3a4f;
  --ink:#0d3b52;
  --gold:#c9a55a;
  --text:#222;
  --faint:#e9edf0;
  --white:#fff;
}
*{margin:0;padding:0;box-sizing:border-box}
html,body{width:1200px;height:3574px;overflow:hidden}
body{position:relative;background:var(--white);font-family:'Lato',sans-serif;color:var(--text)}
h1,h2,h3,h4{font-weight:400}
.abs{position:absolute}

/* header */
.site-header{position:absolute;left:0;top:0;width:1200px;height:92px;background:var(--white);z-index:3}
.brand{position:absolute;left:110px;top:0;width:176px;height:115px;background:var(--white);clip-path:polygon(0 0,100% 0,94% 100%,6% 100%);display:flex;flex-direction:column;align-items:center;justify-content:center;z-index:4}
.brand-name{font-family:'Montserrat',sans-serif;font-weight:600;font-size:19px;letter-spacing:2px;color:var(--ink);line-height:1.1;text-align:center}
.brand-sub{font-family:'Montserrat',sans-serif;font-weight:600;font-size:9px;letter-spacing:3px;color:var(--ink);margin-top:4px}
.nav{position:absolute;top:36px;left:426px;display:flex;align-items:center;font-size:16px;font-family:'Lato',sans-serif;color:#222}
.nav a{color:inherit;text-decoration:none}
.nav a.active{font-weight:700;color:var(--ink)}
.nav .dot{width:5px;height:5px;border-radius:50%;background:#9aa;margin:0 24px}

/* hero */
.hero{position:absolute;left:0;top:92px;width:1200px;height:642px;background:linear-gradient(100deg,#3b3d40 0%,#55585c 40%,#6c7075 62%,#9aa0a6 80%,#4a4c4f 100%)}
.hero-ghost{position:absolute;left:0;width:1200px;text-align:center;font-family:'Open Sans',sans-serif;font-weight:700;font-size:118px;line-height:1.2;color:transparent;-webkit-text-stroke:1px rgba(255,255,255,.25);letter-spacing:2px;white-space:nowrap}
.hero-title{position:absolute;left:0;top:270px;width:1200px;text-align:center;font-family:'Open Sans',sans-serif;font-weight:700;font-size:60px;color:var(--white);letter-spacing:1px}
.dots{position:absolute;top:603px;left:554px;display:flex;gap:10px}
.dots span{width:10px;height:10px;border-radius:50%;border:1px solid rgba(255,255,255,.8)}
.dots span.on{background:var(--white)}

/* section titles */
.ghost{position:absolute;left:0;width:1200px;text-align:center;font-family:'Montserrat',sans-serif;font-weight:300;font-size:104px;line-height:1;white-space:nowrap}
.headline{position:absolute;left:0;width:1200px;display:flex;justify-content:center;align-items:center;gap:18px;font-family:'Montserrat',sans-serif;font-weight:400;font-size:42px;line-height:1}
.headline i{display:block;width:46px;height:3px;margin-top:24px}

/* about */
.about-back{left:134px;top:814px;width:354px;height:456px;background:#eceeef}
.about-photo{left:111px;top:834px;width:358px;height:434px;background:linear-gradient(160deg,#3d5a4d 0%,#bfb8ad 45%,#e2ddd5 75%,#8b8780 100%);box-shadow:0 6px 18px rgba(0,0,0,.2)}
.about-ghost{left:555px;top:836px;font-family:'Montserrat',sans-serif;font-weight:300;font-size:104px;line-height:1;color:var(--faint);white-space:nowrap}
.about-title{left:547px;top:884px;font-family:'Montserrat',sans-serif;font-weight:400;font-size:42px;color:var(--ink);display:flex;align-items:center;gap:14px;line-height:1}
.about-title i{display:block;width:46px;height:3px;background:var(--ink);margin-top:22px}
.about-copy{left:547px;top:950px;width:541px;font-size:16.5px;line-height:30px;text-align:justify;color:#222}
.btn{left:547px;top:1188px;width:137px;height:50px;border-radius:25px;background:var(--gold);color:var(--white);font-weight:700;font-size:16px;display:flex;align-items:center;justify-content:center;text-decoration:none}

/* services */
.services{position:absolute;left:0;top:1384px;width:1200px;height:733px;background:linear-gradient(160deg,#0a4863 0%,#0b4560 60%,#0a3f58 100%)}
.card{position:absolute;top:300px;width:290px;height:319px;background:var(--white);text-align:center;padding:34px 22px 0}
.card.lift{box-shadow:12px 12px 0 rgba(60,110,135,.7)}
.card svg{width:70px;height:70px}
.card h3{font-family:'Montserrat',sans-serif;font-weight:500;font-size:17px;color:#111;margin:22px 0 18px;letter-spacing:.3px}
.card p{font-size:16px;line-height:30px;color:#333}
.arrow{position:absolute;width:30px;height:60px}

/* projects */
.tab{position:absolute;top:2343px;width:222px;height:56px;border-radius:28px;display:flex;align-items:center;justify-content:center;gap:14px;font-family:'Montserrat',sans-serif;font-size:20px}
.tab.on{left:365px;background:var(--gold);color:var(--white);box-shadow:0 6px 14px rgba(0,0,0,.18)}
.tab.off{left:614px;background:var(--white);color:var(--ink);box-shadow:0 3px 12px rgba(0,0,0,.14)}
.shot{position:absolute}

/* footer */
.site-footer{position:absolute;left:0;top:3178px;width:1200px;height:396px;background:var(--navy-deep);color:var(--white)}
.fcol{position:absolute;top:82px}
.fcol h4{font-family:'Montserrat',sans-serif;font-weight:500;font-size:18px;letter-spacing:.5px;margin-bottom:20px}
.fcol ul{list-style:none}
.fcol li{font-size:15.5px;height:30px;display:flex;align-items:center;gap:12px;letter-spacing:.3px;white-space:nowrap}
.chev{width:12px;height:10px}
.contact-row{display:flex;gap:22px;font-size:15.5px;line-height:30px;margin-bottom:14px}
.contact-row svg{width:18px;height:18px;margin-top:6px;flex:none}
.social-dot{width:8px;height:8px;border-radius:50%;background:var(--white)}
.rule{position:absolute;left:111px;top:312px;width:978px;height:1px;background:rgba(255,255,255,.35)}
.copyright{position:absolute;left:0;top:346px;width:1200px;text-align:center;font-size:15px;letter-spacing:.3px}
</style>
</head>
<body>

<header class="site-header">
  <div class="brand">
    <div class="brand-name">ATELIER NINE</div>
    <div class="brand-sub">DESIGN GROUP</div>
  </div>
  <nav class="nav">
    <a class="active" href="#">Home</a><span class="dot"></span>
    <a href="#">About Us</a><span class="dot"></span>
    <a href="#">Team</a><span class="dot"></span>
    <a href="#">Residential</a><span class="dot"></span>
    <a href="#">Commercial</a><span class="dot"></span>
    <a href="#">Contact Us</a>
  </nav>
</header>

<section class="hero" role="img" aria-label="Featured project: dark modern living room with sofa, pendant light and floor-to-ceiling city-view windows">
  <div class="hero-ghost" style="top:170px">ATELIER</div>
  <div class="hero-ghost" style="top:300px">NINE DESIGN</div>
  <h1 class="hero-title">ATELIER NINE DESIGN GROUP</h1>
  <div class="dots"><span></span><span></span><span class="on"></span><span></span><span></span></div>
</section>

<section class="about">
  <div class="abs about-back"></div>
  <div class="abs about-photo" role="img" aria-label="Bright living room with patterned curtains, roman blinds and cream sofa"></div>
  <div class="abs about-ghost">ABOUT US</div>
  <h2 class="abs about-title">WHO WE ARE <i></i></h2>
  <p class="abs about-copy">Lorem ipsum dolor sit amet, consectetur adipiscing elit, sed do eiusmod tempor incididunt ut labore et dolore magna aliqua. Ut enim ad minim veniam, quis nostrud exercitation ullamco laboris nisi ut aliquip ex ea commodo consequat. Duis aute irure dolor in reprehenderit in voluptate velit esse cillum dolore eu fugiat nulla pariatur. Excepteur sint occaecat cupidatat non proident, sunt in culpa qui officia deserunt mollit anim id est laborum.</p>
  <a class="abs btn" href="#">Learn More</a>
</section>

<section class="services">
  <div class="ghost" style="top:100px;color:transparent;-webkit-text-stroke:1.5px rgba(255,255,255,.28)">OUR SERVICES</div>
  <h2 class="headline" style="top:150px;color:var(--gold)"><i style="background:var(--gold)"></i>WHAT WE DO<i style="background:var(--gold)"></i></h2>

  <svg class="arrow" style="left:42px;top:436px" viewBox="0 0 30 60"><path d="M26 4 L4 30 L26 56" fill="none" stroke="#fff" stroke-width="2"/></svg>
  <svg class="arrow" style="left:1130px;top:436px" viewBox="0 0 30 60"><path d="M4 4 L26 30 L4 56" fill="none" stroke="#fff" stroke-width="2"/></svg>

  <article class="card" style="left:111px">
    <svg viewBox="0 0 70 70"><circle cx="52" cy="52" r="16" fill="#e6e6e6"/><rect x="6" y="8" width="50" height="48" fill="none" stroke="#111" stroke-width="2"/><path d="M6 28H30V8M30 40H56M40 40V56M18 28V56" fill="none" stroke="#111" stroke-width="2"/></svg>
    <h3>FROM THE GROUND UP</h3>
    <p>Lorem ipsum damet, consectetur seddo eiusmod tempor incididun ut labore et dolore magna aliqua. Ut enim ad minim veniam.</p>
  </article>
  <article class="card lift" style="left:455px">
    <svg viewBox="0 0 70 70"><circle cx="52" cy="50" r="16" fill="#e6e6e6"/><rect x="6" y="8" width="56" height="38" fill="none" stroke="#111" stroke-width="2"/><path d="M34 46V56M22 58H46M14 16H28V28H14ZM36 18L54 36M54 18L36 36" fill="none" stroke="#111" stroke-width="2"/></svg>
    <h3>MAJOR RENOVATION</h3>
    <p>Lorem ipsum damet, consectetur seddo eiusmod tempor incididun ut labore et dolore magna aliqua. Ut enim ad minim veniam.</p>
  </article>
  <article class="card" style="left:799px">
    <svg viewBox="0 0 70 70"><circle cx="52" cy="50" r="16" fill="#e6e6e6"/><rect x="8" y="34" width="46" height="18" fill="none" stroke="#111" stroke-width="2"/><path d="M12 34V28H50V34M10 52V58M52 52V58M24 8H40V18H24ZM58 12V50M54 12H62" fill="none" stroke="#111" stroke-width="2"/></svg>
    <h3>NEW CONSTRUCTION</h3>
    <p>Lorem ipsum damet, consectetur seddo eiusmod tempor incididun ut labore et dolore magna aliqua. Ut enim ad minim veniam.</p>
  </article>
</section>

<section class="projects">
  <div class="ghost" style="top:2192px;color:var(--faint)">LATEST WORK</div>
  <h2 class="headline" style="top:2246px;color:var(--ink)"><i style="background:var(--ink)"></i>&nbsp;PROJECTS&nbsp;<i style="background:var(--ink)"></i></h2>

  <div class="tab on">
    <svg width="26" height="24" viewBox="0 0 26 24"><path d="M3 11L13 3L23 11M6 9V22H20V9M10 22V15H16V22" fill="none" stroke="#fff" stroke-width="2"/></svg>Residential
  </div>
  <div class="tab off">
    <svg width="26" height="26" viewBox="0 0 26 26"><path d="M4 24V6H14V24M14 12H22V24M2 24H24M8 10V12M8 16V18" fill="none" stroke="#0d3b52" stroke-width="2"/></svg>Commercial
  </div>

  <svg class="arrow" style="left:40px;top:2753px" viewBox="0 0 30 60"><path d="M26 4 L4 30 L26 56" fill="none" stroke="#222" stroke-width="2"/></svg>
  <svg class="arrow" style="left:1130px;top:2753px" viewBox="0 0 30 60"><path d="M4 4 L26 30 L4 56" fill="none" stroke="#222" stroke-width="2"/></svg>

  <div class="shot" style="left:113px;top:2475px;width:449px;height:297px;background:linear-gradient(135deg,#6a6a66 0%,#d8d2c4 50%,#7d7a72 100%)" role="img" aria-label="Study with dark desk, upholstered armchair and shelving"></div>
  <div class="shot" style="left:570px;top:2475px;width:432px;height:297px;background:linear-gradient(135deg,#8a8a8c 0%,#c9c9c9 50%,#f3f3f3 75%,#7a6a62 100%)" role="img" aria-label="Grey marble bathroom with freestanding white bathtub"></div>
  <div class="shot" style="left:313px;top:2782px;width:432px;height:297px;background:linear-gradient(160deg,#6f7d6a 0%,#8a9484 45%,#b57a4e 70%,#4d5441 100%)" role="img" aria-label="Sage green bedroom with upholstered bed and ochre throw"></div>
  <div class="shot" style="left:755px;top:2782px;width:333px;height:297px;background:linear-gradient(135deg,#d8d6d0 0%,#f2f1ee 50%,#9a9d7e 80%,#e8e6e1 100%)" role="img" aria-label="Light bathroom with plants, mirror and bathtub"></div>
</section>

<footer class="site-footer">
  <div class="fcol" style="left:111px">
    <h4>CONTACT</h4>
    <div class="contact-row"><svg viewBox="0 0 18 18"><path d="M9 1C5.7 1 3.5 3.4 3.5 6.4 3.5 10.5 9 17 9 17s5.5-6.5 5.5-10.6C14.5 3.4 12.3 1 9 1z" fill="#fff"/><circle cx="9" cy="6.5" r="2" fill="#0e3a4f"/></svg><span>Atelier Nine Design Group,<br>Address Comes Here</span></div>
    <div class="contact-row"><svg viewBox="0 0 18 18"><path d="M4 2l3 3-1.6 2.2a9 9 0 004.4 4.4L12 10l3 3-2 2.5C7.5 15 3 10.5 2.5 5z" fill="#fff"/></svg><span>+1 555-014-7290</span></div>
    <div class="contact-row"><svg viewBox="0 0 18 18"><rect x="1" y="4" width="16" height="11" fill="#fff"/><path d="M1 4l8 6 8-6" fill="none" stroke="#0e3a4f" stroke-width="1.4"/></svg><span>hello@atelierninedesign.example</span></div>
  </div>
  <div class="fcol" style="left:456px">
    <h4>QUICK LINKS</h4>
    <ul>
      <li><svg class="chev" viewBox="0 0 12 10"><path d="M1 1l4 4-4 4M6 1l4 4-4 4" fill="none" stroke="#fff" stroke-width="1.3"/></svg>Home</li>
      <li><svg class="chev" viewBox="0 0 12 10"><path d="M1 1l4 4-4 4M6 1l4 4-4 4" fill="none" stroke="#fff" stroke-width="1.3"/></svg>About</li>
      <li><svg class="chev" viewBox="0 0 12 10"><path d="M1 1l4 4-4 4M6 1l4 4-4 4" fill="none" stroke="#fff" stroke-width="1.3"/></svg>Team</li>
      <li><svg class="chev" viewBox="0 0 12 10"><path d="M1 1l4 4-4 4M6 1l4 4-4 4" fill="none" stroke="#fff" stroke-width="1.3"/></svg>Residential</li>
      <li><svg class="chev" viewBox="0 0 12 10"><path d="M1 1l4 4-4 4M6 1l4 4-4 4" fill="none" stroke="#fff" stroke-width="1.3"/></svg>Commercial</li>
    </ul>
  </div>
  <div class="fcol" style="left:696px">
    <h4>OTHER LINKS</h4>
    <ul>
      <li><svg class="chev" viewBox="0 0 12 10"><path d="M1 1l4 4-4 4M6 1l4 4-4 4" fill="none" stroke="#fff" stroke-width="1.3"/></svg>Terms &amp; Condition</li>
      <li><svg class="chev" viewBox="0 0 12 10"><path d="M1 1l4 4-4 4M6 1l4 4-4 4" fill="none" stroke="#fff" stroke-width="1.3"/></svg>Privacy Policy</li>
      <li><svg class="chev" viewBox="0 0 12 10"><path d="M1 1l4 4-4 4M6 1l4 4-4 4" fill="none" stroke="#fff" stroke-width="1.3"/></svg>Cookies</li>
      <li><svg class="chev" viewBox="0 0 12 10"><path d="M1 1l4 4-4 4M6 1l4 4-4 4" fill="none" stroke="#fff" stroke-width="1.3"/></svg>Contact Us</li>
    </ul>
  </div>
  <div class="fcol" style="left:964px">
    <h4>OTHER LINKS</h4>
    <ul>
      <li><span class="social-dot"></span>Pinboard Social</li>
      <li><span class="social-dot"></span>Chirpline</li>
      <li><span class="social-dot"></span>Snapgrid</li>
    </ul>
  </div>
  <div class="rule"></div>
  <p class="copyright">2022 Atelier Nine Design Group. All Rights Reserved.</p>
</footer>

</body>
</html>
```